Simple elegant business card

General card for a fin and television director.
Just want name, email, phone and address.

Target Market(s)

Prospective employers

Industry/Entity Type

Business

Requirements
Must have
• As above
Nice to have
• Logo but not necessary.
Should not have
• Not too colourful or funky.
• Simplicity and elegance the way to go.

```html
<!DOCTYPE html>
<html lang="en">
<head>
<meta charset="utf-8">
<title>Nora Hale — Business Cards</title>
<link href="https://fonts.googleapis.com/css2?family=Quicksand:wght@300&display=swap" rel="stylesheet">
<style>
  :root {
    --canvas-bg: #ffffff;
    --light-center: #ffffff;
    --light-edge: #c6c7c9;
    --dark-center: #56575a;
    --dark-edge: #000000;
    --sprocket: #ffffff;
    --light-text: #55565a;
    --light-rule: #8fa3bd;
    --dark-text: #e6e6e8;
    --dark-rule: #9a9b9e;
  }
  * { margin: 0; padding: 0; box-sizing: border-box; }
  html, body { width: 1200px; height: 1000px; overflow: hidden; background: var(--canvas-bg); }
  .canvas { position: relative; width: 1200px; height: 1000px; }
  .card {
    position: absolute; left: 308px; width: 596px; height: 344px;
    font-family: "Quicksand", sans-serif;
    font-weight: 300;
  }
  .card--light {
    top: 120px;
    background: radial-gradient(ellipse 300px 230px at 50% 52%, var(--light-center) 0%, var(--light-edge) 100%);
    color: var(--light-text);
  }
  .card--dark {
    top: 546px;
    background: radial-gradient(ellipse 320px 240px at 50% 48%, var(--dark-center) 0%, var(--dark-edge) 100%);
    color: var(--dark-text);
  }
  .sprockets { position: absolute; top: 13px; width: 44px; }
  .sprockets--left { left: 19px; }
  .sprockets--right { left: 533px; }
  .sprocket {
    width: 44px; height: 27px; margin-bottom: 21px;
    background: var(--sprocket); border-radius: 6px;
  }
  .name, .contact {
    position: absolute; left: 0; width: 100%; text-align: center;
    font-weight: 300;
    -webkit-font-smoothing: antialiased;
    -moz-osx-font-smoothing: grayscale;
    will-change: transform;
    transform: translateZ(0);
  }
  .name { font-size: 31px; letter-spacing: 0.6px; line-height: 1; }
  .contact { font-size: 22px; line-height: 27px; letter-spacing: 0.2px; }
  .rule { position: absolute; left: 188px; width: 218px; height: 1px; }
  .card--light .rule { background: var(--light-rule); }
  .card--dark .rule { background: var(--dark-rule); }
  .card--light .name { top: 117px; }
  .card--light .rule { top: 232px; }
  .card--light .contact { top: 242px; }
  .card--dark .name { top: 128px; }
  .card--dark .rule { top: 175px; }
  .card--dark .contact { top: 188px; }
</style>
</head>
<body>
<div class="canvas">
  <section class="card card--light">
    <div class="sprockets sprockets--left">
      <div class="sprocket"></div><div class="sprocket"></div><div class="sprocket"></div><div class="sprocket"></div><div class="sprocket"></div><div class="sprocket"></div><div class="sprocket"></div>
    </div>
    <div class="sprockets sprockets--right">
      <div class="sprocket"></div><div class="sprocket"></div><div class="sprocket"></div><div class="sprocket"></div><div class="sprocket"></div><div class="sprocket"></div><div class="sprocket"></div>
    </div>
    <h1 class="name">Nora Hale</h1>
    <div class="rule"></div>
    <p class="contact">norahale@mail.com<br>+1 555 204 8817<br>48 Elm Row, Los Angeles</p>
  </section>

  <section class="card card--dark">
    <div class="sprockets sprockets--left">
      <div class="sprocket"></div><div class="sprocket"></div><div class="sprocket"></div><div class="sprocket"></div><div class="sprocket"></div><div class="sprocket"></div><div class="sprocket"></div>
    </div>
    <div class="sprockets sprockets--right">
      <div class="sprocket"></div><div class="sprocket"></div><div class="sprocket"></div><div class="sprocket"></div><div class="sprocket"></div><div class="sprocket"></div><div class="sprocket"></div>
    </div>
    <h1 class="name">Nora Hale</h1>
    <div class="rule"></div>
    <p class="contact">norahale@mail.com<br>+1 555 204 8817<br>48 Elm Row, Los Angeles</p>
  </section>
</div>
</body>
</html>
```